Give us a remarkable appearance

We need a unique, remarkable stationery design (Business Cards, Business Letters, Email Signature etc.). The design should use our logo.

Veltro-Consulting is a startup in consulting, management and IT services and individual software development for the financial industry.

Veltro in english is agate stone. We would like to see designs that use colors out of the agate stone color range.

Preferred COLORS: gold, dark red (burgundy), white, dark grey, black ** see attached Logos **

The used font should be available for further usage with texts etc.

The design should express: modernity, precious, high quality, lightness, stability, ecological awareness, speedy, reliability, simplicity, sustainability.

Target Market(s)

C-Level and Business Clients, Professionals

Industry/Entity Type

Business

Logo Text

Logo styles of interest
Pictorial/Combination Logo
Abstract Logo
Wordmark Logo
Requirements
Must have
• Business Cards, Business Papers, Email Signature
Nice to have
• Door plate, Flyersheet (basic structure), Envelop...

```html
<!DOCTYPE html>
<html lang="en">
<head>
<meta charset="utf-8">
<title>Veltro Consulting – Business Cards</title>
<link href="https://fonts.googleapis.com/css2?family=Jost:wght@400;500;600;700&display=swap" rel="stylesheet">
<style>
  :root {
    --backdrop: #c9c9c7;
    --gold-deep: #b47d14;
    --gold-mid: #c89418;
    --gold-glow: #e2b523;
    --gold-text: #c08a12;
    --ink: #1f1f1f;
    --paper: #ffffff;
    --paper-shade: #ececeb;
  }
  * { box-sizing: border-box; margin: 0; padding: 0; }
  html, body {
    width: 1200px;
    height: 900px;
    overflow: hidden;
    background: var(--backdrop);
    font-family: "Jost", "Futura", sans-serif;
  }
  .stationery {
    position: relative;
    width: 1200px;
    height: 900px;
  }
  .card {
    position: absolute;
    width: 588px;
    height: 336px;
    border-radius: 3px;
    box-shadow: 0 10px 30px rgba(0,0,0,0.18);
    overflow: hidden;
  }
  /* Front side */
  .card-front {
    left: 110px;
    top: 90px;
    background: radial-gradient(ellipse 55% 60% at 50% 42%, var(--gold-glow) 0%, var(--gold-mid) 55%, var(--gold-deep) 100%);
    color: var(--paper);
  }
  .front-brand {
    position: absolute;
    left: 0;
    right: 0;
    top: 120px;
    display: flex;
    align-items: center;
    justify-content: center;
    gap: 14px;
    font-size: 34px;
    font-weight: 600;
    letter-spacing: 1px;
  }
  .brand-dot {
    width: 18px;
    height: 18px;
    border-radius: 50%;
    background: currentColor;
  }
  .front-web {
    position: absolute;
    left: 0;
    right: 0;
    bottom: 44px;
    text-align: center;
    font-size: 15px;
    font-weight: 400;
    letter-spacing: 0.3px;
  }
  .front-web strong { font-weight: 600; }
  /* Back side */
  .card-back {
    left: 500px;
    top: 470px;
    background: linear-gradient(120deg, var(--paper) 0%, var(--paper) 55%, var(--paper-shade) 100%);
    color: var(--ink);
  }
  .back-brand {
    position: absolute;
    left: 44px;
    top: 48px;
    display: flex;
    align-items: center;
    gap: 12px;
    font-size: 30px;
    font-weight: 600;
    color: var(--gold-text);
    letter-spacing: 0.5px;
  }
  .brand-square {
    width: 16px;
    height: 16px;
    background: currentColor;
  }
  .contact {
    position: absolute;
    left: 44px;
    top: 190px;
    font-size: 15px;
    line-height: 1.35;
  }
  .holder {
    display: flex;
    align-items: center;
    margin-bottom: 18px;
  }
  .holder-name {
    font-size: 20px;
    font-weight: 700;
    color: var(--gold-text);
    padding-right: 6px;
    border-right: 1.5px solid var(--ink);
  }
  .holder-role {
    padding-left: 6px;
    font-size: 14px;
    font-weight: 500;
  }
  .contact-line {
    display: flex;
    align-items: center;
    gap: 5px;
  }
  .contact-line svg { width: 14px; height: 12px; fill: var(--gold-text); }
  .phones { gap: 4px; }
  .phone-item { display: inline-flex; align-items: center; gap: 4px; }
</style>
</head>
<body>
<main class="stationery">
  <section class="card card-front" aria-label="Business card front">
    <div class="front-brand"><span class="brand-dot"></span>Veltro Consulting</div>
    <p class="front-web">www.<strong>veltroconsulting</strong>.com</p>
  </section>

  <section class="card card-back" aria-label="Business card back">
    <div class="back-brand"><span class="brand-square"></span>Veltro Consulting</div>
    <div class="contact">
      <div class="holder">
        <span class="holder-name">Daniel Mercer</span>
        <span class="holder-role">Publisher</span>
      </div>
      <p class="contact-line">48, Harbor Lane, Eastfield, Country, 210.</p>
      <p class="contact-line phones">
        <span class="phone-item">
          <svg viewBox="0 0 14 12" aria-hidden="true"><path d="M1 4c0-2 2-3 6-3s6 1 6 3l-3 1-1-2H5L4 5zM3 6h8l2 5H1z"/></svg>262-555-0148
        </span>
        <span class="phone-item">
          <svg viewBox="0 0 14 12" aria-hidden="true"><path d="M1 4c0-2 2-3 6-3s6 1 6 3l-3 1-1-2H5L4 5zM3 6h8l2 5H1z"/></svg>877-555-0192
        </span>
      </p>
      <p class="contact-line">
        <svg viewBox="0 0 14 12" aria-hidden="true"><path d="M1 2h12v8H1zM2 3l5 4 5-4v1L7 8 2 4z" fill-rule="evenodd"/></svg>mercer@veltroconsulting.com
      </p>
    </div>
  </section>
</main>
</body>
</html>
```